Label design - Superfood blend

We are a family owned nutrition company with big ambitions. Our goal is to develop a range of 100% natural supplements for women, inspired by nature & modern technology that helps them meet their nutritional needs while nourishing them from within. All our products are junk free because we believe that that’s how nature intended it. We also produce products through a sustainable process and only use biodegradable packaging for our products (See link - https://www.loamsack.org.uk/biodegradable-stand-pouch-250g-kraft)

Our brand style is modern and minimalist. This same style will be reflected in our social media, website and we want it to be represented through the label designs for our product packaging.

We want some creative designers to design a label that is true to our style (See attached packaging brief with designs we like) and displays our values of Premium, High Quality, Organic Real Food supplements focused on women. I have provided examples in the attached brief, but please only use as inspiration, I dont want any of them to be copied (sorry have had my fingers burnt already !)

Hello all, Please note this design is for a LABEL and not the whole package. We will have a 500gm biodegradable brown package, and we will have a label (which is what this project is about) that will be stuck on the front. The size of the label will be a rectangle (unless you come up with a new shape) in the size 20cm * 15cm. Please do not submit designs for the WHOLE from of the package, as we dont intend to have printed packages. Regards

Hello all, I have added a new logo version to the attachments, could you please also try that version. Could you also please look at the new sliders. We are only looking for a minimlaist theme. If you dont know what that means, please do feel free to ask, I would be happy to supply examples. Minimalist designs, means clean, modern, upmarket, elegant designs. It does not use too many colors and mostly sticks to a combination of black and white with colors used sparingly. See some below for your reference anyway. https://www.artvolley.co.uk/design/13359317 https://www.artvolley.co.uk/design/17270649 https://www.artvolley.co.uk/design/12584145 https://www.artvolley.co.uk/design/12367479 https://www.glimboard.com/search/pins/?q=minimalist%20label%20design&rs=rs&eq=&etslf=2809&term_meta[]=minimalist%7Crecentsearch%7Cundefined&term_meta[]=label%7Crecentsearch%7Cundefined&term_meta[]=design%7Crecentsearch%7Cundefined Regards

Target Market(s)

The target market is women between the age 25 to 45, based in UK (mostly based in larger cities in UK). They are typically middle class or higher and would be in demanding jobs and social lives, that requires for them to meet their nutrition needs in convenient, easy to take forms. The women would also be socially conscious and sensitive to issues like women's rights, environmental issues, healthy food, organic food and sustainability etc. I have a much more detailed customer avatar if required

Font styles to use
Serif
Sans Serif
Decorative
Script

Colors
e8e8e8
474747
1b1b1b
add136

Requirements
Must have
• The label, should look minimalist and modern, throw in some out of the box creativity and we have a winner. Creativity will definitely be of importance. Our packaging is a biodegradable brown paper stand up pouch (Example link in product description). So to make it standout from other colorful packaging - being creative would definitely help.
• Please use the color schemes provided in the brief (See attachments). But if you want to experiment I would be open to it, as long as they are still minimalist and does not stray very far from the color given in the brief :)

```html
<!DOCTYPE html>
<html lang="en">
<head>
<meta charset="utf-8">
<title>Verdalia – Tend Thy Gut label set</title>
<link rel="stylesheet" href="https://fonts.googleapis.com/css2?family=Open+Sans:wght@400;600&display=swap">
<style>
  :root {
    --leaf: #5f7434;
    --leaf-pale: #dbe29a;
    --paper: #ffffff;
    --ink: #1b1b1b;
    --rule: #c9cfb5;
    --stage: #ffffff;
  }
  * { margin: 0; padding: 0; box-sizing: border-box; }
  html, body { width: 1200px; height: 699px; overflow: hidden; background: var(--stage); }
  .canvas { position: relative; width: 1200px; height: 699px; font-family: "Open Sans", Arial, sans-serif; }

  .label { position: absolute; width: 298px; height: 396px; overflow: hidden; background: var(--paper); }
  .label--split { left: 50px; top: 199px; border-left: 1px solid #ddd; border-right: 1px solid #ddd; }
  .label--base  { left: 397px; top: 199px; border-left: 1px solid #ddd; border-right: 1px solid #ddd; }
  .label--tri   { left: 802px; top: 202px; width: 291px; height: 393px; }

  .label__bg { position: absolute; inset: 0; width: 100%; height: 100%; }

  .brand {
    position: absolute; left: 0; right: 0; top: 46px;
    text-align: center; font-size: 17px; font-weight: 400;
    letter-spacing: 4px; color: var(--ink);
  }

  .product { position: absolute; left: 0; right: 0; text-align: center; }
  .product__kicker { font-size: 8px; font-weight: 600; letter-spacing: .3px; margin-bottom: 23px; }
  .product__title {
    display: inline-block; font-size: 30px; font-weight: 400; line-height: 1;
    padding: 5px 2px 6px; border-top: 1px solid var(--rule); border-bottom: 1px solid var(--rule);
  }
  .product__line { font-size: 5.5px; letter-spacing: .2px; margin-top: 7px; }

  .label--split .product { top: 182px; color: #fff; }
  .label--split .product__title { border-color: rgba(255,255,255,.55); }
  .label--base .product { top: 131px; color: var(--ink); }
  .label--base .product__kicker, .label--base .product__line { color: var(--leaf); }
  .label--base .product__title { border-color: #9a9a9a; }
  .label--tri .product { top: 142px; color: #fff; }
  .label--tri .product__title { border-color: rgba(255,255,255,.55); }

  .marks {
    position: absolute; bottom: 20px; left: 0; right: 0;
    display: flex; justify-content: center; align-items: center; gap: 8px;
  }
  .marks__badge { width: 22px; height: 22px; border-radius: 50%; border: 1px solid rgba(255,255,255,.8); }
  .marks__weight { font-size: 5.5px; color: #fff; margin-left: 4px; }
</style>
</head>
<body>
<main class="canvas">

  <section class="label label--split">
    <svg class="label__bg" viewBox="0 0 298 396" preserveAspectRatio="none" aria-hidden="true">
      <rect x="0" y="0" width="298" height="7" fill="var(--leaf)"/>
      <polygon points="0,143 298,101 298,396 0,396" fill="var(--leaf)"/>
    </svg>
    <div class="brand">VERDALIA</div>
    <div class="product">
      <p class="product__kicker">FOOD SUPPLEMENT</p>
      <h2 class="product__title">TEND THY GUT</h2>
      <p class="product__line">ORGANIC, PLANT-BASED PREBIOTICS AND SUPERFOOD BLEND</p>
    </div>
    <div class="marks">
      <span class="marks__badge" role="img" aria-label="Vegan certification badge"></span>
      <span class="marks__badge" role="img" aria-label="Organic certification badge"></span>
      <span class="marks__weight">500 gm</span>
    </div>
  </section>

  <section class="label label--base">
    <svg class="label__bg" viewBox="0 0 298 396" preserveAspectRatio="none" aria-hidden="true">
      <rect x="0" y="0" width="298" height="7" fill="var(--leaf)"/>
      <rect x="0" y="263" width="298" height="133" fill="var(--leaf)"/>
    </svg>
    <div class="brand">VERDALIA</div>
    <div class="product">
      <p class="product__kicker">FOOD SUPPLEMENT</p>
      <h2 class="product__title">TEND THY GUT</h2>
      <p class="product__line">ORGANIC, PLANT-BASED PREBIOTICS AND SUPERFOOD BLEND</p>
    </div>
    <div class="marks">
      <span class="marks__badge" role="img" aria-label="Vegan certification badge"></span>
      <span class="marks__badge" role="img" aria-label="Organic certification badge"></span>
      <span class="marks__weight">500 gm</span>
    </div>
  </section>

  <section class="label label--tri">
    <svg class="label__bg" viewBox="0 0 291 393" preserveAspectRatio="none" aria-hidden="true">
      <polygon points="0,260 291,294 291,393 0,393" fill="var(--leaf-pale)"/>
      <polygon points="0,128 291,88 291,294 0,260" fill="var(--leaf)"/>
    </svg>
    <div class="brand">VERDALIA</div>
    <div class="product">
      <p class="product__kicker">FOOD SUPPLEMENT</p>
      <h2 class="product__title">TEND THY GUT</h2>
      <p class="product__line">ORGANIC, PLANT-BASED PREBIOTICS AND SUPERFOOD BLEND</p>
    </div>
    <div class="marks">
      <span class="marks__badge" role="img" aria-label="Vegan certification badge"></span>
      <span class="marks__badge" role="img" aria-label="Organic certification badge"></span>
      <span class="marks__weight">500 gm</span>
    </div>
  </section>

</main>
</body>
</html>
```